RUVTOM IT Limited Buisness card logo

I am setting up a IT Consultancy company and want a logo that is related to the IT industry, but also i am thinking that the A in RUV and the A in TOM are linked together maybe horizontally and vertically, also thought about the A being @ as it symbolises IT services. This logo will be used on paperwork, business cards and website.

Industry/Entity Type

Business

Contact Information for Business Card

Gerald Whitmore
RUVTOM IT Limited
IT Consultant
Mobile: 07915362480
Email: geraldvw@mailbryn.co.uk

Requirements
Must have
• IT Theme

```html
<!DOCTYPE html>
<html lang="en">
<head>
<meta charset="utf-8">
<title>RUVTOM IT Limited – Business Card</title>
<link rel="stylesheet" href="https://fonts.googleapis.com/css2?family=Arimo:wght@400;700&display=swap">
<style>
  :root {
    --backdrop: #1f1b1b;
    --card-top: #1b74d6;
    --card-mid: #1a4fb3;
    --card-bottom: #1e2a86;
    --ink: #ffffff;
    --accent-bar: #5fb2f2;
  }
  * { margin: 0; padding: 0; box-sizing: border-box; }
  html, body {
    width: 1200px;
    height: 709px;
    overflow: hidden;
    background: var(--backdrop);
  }
  .canvas {
    position: relative;
    width: 1200px;
    height: 709px;
    background: var(--backdrop);
  }
  .business-card {
    position: absolute;
    left: 138px;
    top: 98px;
    width: 853px;
    height: 500px;
    overflow: hidden;
    background: linear-gradient(180deg, var(--card-top) 0%, var(--card-mid) 45%, var(--card-bottom) 100%);
    font-family: "Arimo", Arial, sans-serif;
    color: var(--ink);
  }
  .network-artwork {
    position: absolute;
    left: 0;
    top: 0;
    width: 853px;
    height: 230px;
    background:
      radial-gradient(circle at 560px 30px, rgba(159, 212, 255, 0.55) 0, rgba(80, 160, 240, 0.35) 120px, rgba(27, 116, 214, 0) 175px),
      radial-gradient(ellipse 420px 110px at 180px 90px, rgba(220, 240, 255, 0.28) 0, rgba(27, 116, 214, 0) 100%);
  }
  .contact {
    position: absolute;
    right: 511px;
    top: 206px;
    text-align: right;
    white-space: nowrap;
  }
  .contact__name {
    font-weight: 700;
    font-size: 30px;
    line-height: 34px;
    margin-bottom: 6px;
  }
  .contact__line {
    font-weight: 400;
    font-size: 21px;
    line-height: 28px;
  }
  .divider {
    position: absolute;
    left: 359px;
    top: 215px;
    width: 6px;
    height: 249px;
    background: var(--accent-bar);
  }
  .brand {
    position: absolute;
    left: 386px;
    top: 366px;
    white-space: nowrap;
  }
  .brand__name {
    font-weight: 700;
    font-size: 62px;
    line-height: 62px;
    letter-spacing: 29px;
    color: var(--ink);
  }
  .brand__tagline {
    font-weight: 700;
    font-size: 34px;
    line-height: 38px;
    color: var(--ink);
  }
</style>
</head>
<body>
  <main class="canvas">
    <section class="business-card">
      <div class="network-artwork" role="img" aria-label="Glowing globe with streaks of light from fibre-optic data lines"></div>

      <div class="contact">
        <p class="contact__name">Gerald Whitmore</p>
        <p class="contact__line">07915362480</p>
        <p class="contact__line">geraldvw@mailbryn.co.uk</p>
      </div>

      <div class="divider"></div>

      <div class="brand">
        <p class="brand__name">RUVTOM</p>
        <p class="brand__tagline">IT Limited IT Consultant</p>
      </div>
    </section>
  </main>
</body>
</html>
```